Postcard Design

Lumen Petal a Waxing Boutique - We need a postcard Front of it with a boarder done as a dainty picture frame and inside listing our services menu. We would like the picture frame to be white and the background to be a light grey and service menu writing in white as well. On back we need name, address, etc. We weould like the name to be in Turquise. Do you help design logos?
menu sheet -
Facial Services:
Brow Shaping $18
Lip - $12
Brow and Lip Combo $25
Sideburns - $12
Nose $10
Ears $10
Full Face Combo Excluding Brows $40
Full Face Combo w/ Brow Shaping $55
Lash Tint $20
Brow Tint $15
(This is to darken brows only)
Brow Shaping + Brow Tint $33

BODY WAXING :
Neck $15
Shoulders$20
Full back $45
Chest $45
(Abdomen Included)
Abdomen $15
Underarms $15
Full Arm $40
Half Arm $30
Full Leg $60
(Bikini line not included, This covers the upper thigh down to the feet and toes)
Half Leg $45
(Upper or Lower leg)
Modest Bikini - $35 Female Only
Brazilian Bikini $55 Female Only
Buttocks $20

Whats So Special About Our Pricing? Its Simple:
*Straight Forward Prices and No Tipping Policy!

Back of Card -

Lumen Petal
{Waxing Boutique}

Located in Studios Corvana
412 W. Tobin Creek Pkwy
Suite 17
Rockwall, TX 75519
(972)555-0148

```html
<!DOCTYPE html>
<html lang="en">
<head>
<meta charset="utf-8">
<title>Lumen Petal a Waxing Boutique – Services Menu</title>
<link href="https://fonts.googleapis.com/css2?family=Catamaran:wght@600;700;800&family=Sniglet:wght@800&display=swap" rel="stylesheet">
<style>
  :root {
    --card-grey: #dfe1e2;
    --frame-white: #ffffff;
    --accent-red: #f0311e;
    --ink: #1b1b1b;
    --photo-skin: #e9b7a8;
    --photo-skin-deep: #d99a86;
    --photo-green: #b9b04a;
  }
  html, body {
    margin: 0;
    padding: 0;
    width: 1200px;
    height: 930px;
    overflow: hidden;
    background: var(--card-grey);
  }
  .postcard {
    position: relative;
    width: 1200px;
    height: 930px;
    background: var(--card-grey);
    font-family: "Catamaran", sans-serif;
    color: var(--ink);
  }
  .frame {
    position: absolute;
    inset: 0;
  }
  .photo {
    position: absolute;
    border-radius: 50%;
  }
  .photo-arm { left: 101px; top: 91px; width: 200px; height: 200px;
    background: radial-gradient(circle at 40% 40%, #f6e3de, var(--photo-skin)); }
  .photo-lip { left: 319px; top: 148px; width: 148px; height: 148px;
    background: radial-gradient(circle at 45% 45%, var(--photo-green), var(--photo-skin-deep) 70%); }
  .photo-brow { left: 754px; top: 150px; width: 144px; height: 144px;
    background: radial-gradient(circle at 50% 45%, #f3d3c4, var(--photo-skin)); }
  .photo-leg { left: 918px; top: 91px; width: 200px; height: 200px;
    background: radial-gradient(circle at 60% 50%, #f1c2ad, var(--photo-skin-deep)); }
  .name-pennant {
    position: absolute;
    left: 468px;
    top: 0;
    width: 281px;
    height: 222px;
  }
  .brand-name {
    position: absolute;
    left: 468px;
    top: 108px;
    width: 281px;
    text-align: center;
    font-weight: 800;
    font-size: 40px;
    color: var(--accent-red);
    line-height: 1;
    text-transform: uppercase;
  }
  .menu-section {
    position: absolute;
    left: 0;
    width: 1200px;
    text-align: center;
  }
  .menu-heading {
    margin: 0;
    font-weight: 800;
    font-size: 35px;
    line-height: 1;
    color: var(--accent-red);
    display: inline-block;
    border-bottom: 3px solid var(--accent-red);
    padding-bottom: 1px;
  }
  .menu-line {
    margin: 0;
    font-weight: 700;
    font-size: 22px;
    line-height: 41.5px;
    text-transform: uppercase;
    white-space: nowrap;
  }
  .note { color: var(--accent-red); font-weight: 600; }
  .body-waxing { top: 283px; }
  .body-waxing .menu-list { margin-top: 4px; }
  .facial-services { top: 550px; }
  .facial-services .menu-list { margin-top: 6px; }
  .facial-services .menu-line { line-height: 46.5px; }
  .policy-ribbon {
    position: absolute;
    left: 129px;
    top: 733px;
    width: 925px;
    height: 83px;
  }
  .policy-text {
    position: absolute;
    left: 129px;
    top: 733px;
    width: 925px;
    height: 66px;
    line-height: 66px;
    text-align: center;
    font-family: "Sniglet", sans-serif;
    font-weight: 800;
    font-size: 25px;
    color: var(--frame-white);
    text-transform: uppercase;
  }
</style>
</head>
<body>
<main class="postcard">
  <svg class="frame" width="1200" height="930" viewBox="0 0 1200 930" aria-hidden="true">
    <g fill="none" stroke="var(--frame-white)">
      <rect x="28" y="22" width="1144" height="886" stroke-width="9"/>
      <rect x="48" y="40" width="1104" height="850" stroke-width="4"/>
    </g>
  </svg>

  <div class="photo photo-arm" role="img" aria-label="Photo of wax being applied to an arm with a spatula"></div>
  <div class="photo photo-lip" role="img" aria-label="Photo of green wax applied above the lip"></div>
  <div class="photo photo-brow" role="img" aria-label="Photo of a freshly shaped eyebrow"></div>
  <div class="photo photo-leg" role="img" aria-label="Photo of smooth legs with a pink lily"></div>

  <svg class="name-pennant" width="281" height="222" viewBox="0 0 281 222" aria-hidden="true">
    <polygon points="0,0 281,0 281,196 141,222 0,196" fill="var(--frame-white)"/>
  </svg>
  <div class="brand-name">Lumen Petal</div>

  <section class="menu-section body-waxing">
    <h2 class="menu-heading">BODY WAXING :</h2>
    <div class="menu-list">
      <p class="menu-line">Neck $15, Shoulders$20, Full Back $45, Chest $45(Abdomen Included)</p>
      <p class="menu-line">Abdomen $15, Underarms $15, Full Arm $40, Half Arm $30, Full Leg $60</p>
      <p class="menu-line"><span class="note">(Bikini line not included, this covers the upper thigh down to the feet</span></p>
      <p class="menu-line"><span class="note">and toes)</span>Half Leg $45,<span class="note">(Upper or Lower Leg)</span>&nbsp; Modest Bikini - $35 Female</p>
      <p class="menu-line">Only Brazilian Bikini $55 Female Only, Buttocks $20</p>
    </div>
  </section>

  <section class="menu-section facial-services">
    <h2 class="menu-heading">FACIAL SERVICES:</h2>
    <div class="menu-list">
      <p class="menu-line">Brow Shaping $18, Lip - $12, Brow and Lip Combo $25</p>
      <p class="menu-line">Sideburns - $12, Nose $10, Ears $10, Full Face Combo Excluding Brows $40</p>
      <p class="menu-line">Full Face Combo w/ Brow Shaping $55, Lash Tint $20, Brow Tint $15</p>
    </div>
  </section>

  <svg class="policy-ribbon" width="925" height="83" viewBox="0 0 925 83" aria-hidden="true">
    <polygon points="0,0 925,0 895,33 925,66 0,66 30,33" fill="var(--accent-red)"/>
  </svg>
  <p class="policy-text" style="margin:0">Straight Forward Prices and No Tipping Policy!</p>
</main>
</body>
</html>
```